Ringbeacon Hub - Web design / template design

Hello,

I need a design for my existing site. I already have a logo that I want to use, which you can find on my site ( I can also provide different formats / larger versions ).

Please see http://www.ringbeaconhub.example for details of the site.

What I need are pages with sections that can be edited, so for example, I need basic table / div content sections that I can place in the members area that can contain whatever custom content I need to put in them without the table / div design getting stretched out or skewed.

The main page, basically needs to have all of the content on the current page or room for it at least should I want to add it.

You can also see ww2.ringbeaconhub.example with more info ( not a live site and me trying my best to do something, but I'm just not good at design :)

The site content for the most part needs to be actual text, rather than text on images. I will need to change this content and have it indexed by search engines, if you want, you can just put filler text in. There are exceptions of course, like maybe on the main page, if there are boxes with some static image text, that is fine.

Target Market(s)

Telephony, phone service providers, phone system users

Industry/Entity Type

It Service

Requirements
Must have
• Dynamic content capabilities.

Logo colors implemented in the site in some way.

Easy navigation ( tabs at the top are good or whatever you think ).

I will have the following sections:

1. Home
2. About us ( company info ).
3. How to / Help
4. Pricing
5. Support section.
6. Contact section
7. Singup section
8. Members section

I would like the main page to be more image / wow factor and the other pages really just need to be basic layout and places to put tables or divs with content in them. Table or div header images are for titles are ok as long as I can edit them.

Nice to have
• Sign up button placed somewhere.

Chirpline / Friendwall / LinkedIn buttons

Should not have
• Flash or all page content in static images.

```html
<!DOCTYPE html>
<html lang="en">
<head>
<meta charset="utf-8">
<title>Ringbeacon Hub – VoIP CNAM Service Provider</title>
<link href="https://fonts.googleapis.com/css2?family=Arimo:wght@400;700&display=swap" rel="stylesheet">
<style>
:root{
  --page-bg:#d3e0e6;
  --header-bg:#fafbfc;
  --ink-blue:#1f3e8c;
  --brand-blue:#4e72a8;
  --nav-top:#5aa2f0;
  --nav-bottom:#2a74d6;
  --green-top:#7fd41a;
  --green-bottom:#2f9a0a;
  --panel-line:#c4cbd3;
  --box-line:#8f9aa8;
  --red:#e0141a;
  --orange-top:#f7a640;
  --orange-bottom:#fde7a8;
  --row-top:#c9d3ec;
  --row-bottom:#9fb0da;
}
*{box-sizing:border-box;margin:0;padding:0}
html,body{width:1177px;height:1200px;overflow:hidden}
body{background:var(--page-bg);font-family:"Arimo",Arial,sans-serif;color:var(--ink-blue);position:relative}
.site-header{position:absolute;left:0;top:0;width:1177px;height:108px;background:var(--header-bg);border-bottom:2px solid #e6ebee}
.brand{position:absolute;left:117px;top:36px;display:flex;align-items:center;gap:10px}
.brand-dot{width:18px;height:18px;border-radius:50%;background:#7cc41f}
.brand-name{font-size:34px;font-weight:700;color:#2a6fd0;letter-spacing:-.5px}
.tagline{position:absolute;right:127px;top:26px;text-align:right;color:var(--brand-blue);font-weight:700}
.tagline .site{font-size:17px;display:block}
.tagline .role{font-size:23px;display:block;margin-top:2px}
.sheet{position:absolute;left:118px;top:126px;width:941px;height:1074px;background:#fff}
.main-nav{position:absolute;left:0;top:0;width:941px;height:47px;display:flex;background:linear-gradient(var(--nav-top),var(--nav-bottom))}
.main-nav a{display:flex;align-items:center;justify-content:center;color:#fff;font-size:19px;text-decoration:none;border-right:1px solid #7fb7f2;height:100%}
.main-nav a.active{background:linear-gradient(var(--green-top),var(--green-bottom));color:#0c1a05;font-weight:700}
.content-panel{position:absolute;left:8px;top:57px;width:620px;height:952px;border:1px solid var(--panel-line);border-radius:10px;background:linear-gradient(170deg,#fff 0%,#f3f6f8 45%,#e9eef1 100%);padding:18px 12px 0 27px}
.content-panel h1{font-size:23px;color:var(--ink-blue);margin-bottom:14px}
.content-panel p{font-size:12px;line-height:14px;margin-bottom:14px;color:var(--ink-blue)}
.accent{color:var(--red)}
.info-box{position:absolute;left:63px;width:532px;border:1px solid var(--box-line);background:rgba(236,241,245,.8);box-shadow:2px 2px 2px rgba(0,0,0,.15);padding:24px 20px 4px 23px}
.info-box p{margin-bottom:14px}
.info-tab{position:absolute;left:-19px;top:-23px;height:40px;padding:0 15px;background:linear-gradient(var(--green-top),var(--green-bottom));color:#0c1a05;font-weight:700;font-size:16px;display:flex;align-items:center}
.info-tab::after{content:"";position:absolute;left:0;bottom:-12px;border-top:12px solid #333;border-left:19px solid transparent}
.signup{position:absolute;left:626px;top:57px;width:312px;height:436px;border:1px solid #2a64c4;background:#fff}
.signup-head{height:90px;background:linear-gradient(var(--green-top),var(--green-bottom));text-align:center;padding-top:4px}
.signup-head .big{font-size:46px;font-weight:700;color:var(--red);line-height:46px;display:block}
.signup-head .small{font-size:29px;font-weight:700;color:#0c1a05;line-height:32px;display:block}
.field{position:absolute;left:14px;width:282px;height:38px;border:1px solid #b9a99a;font-size:11.5px;color:#555;padding:13px 9px}
.field.tall{height:91px}
.signup-btn{position:absolute;left:87px;top:383px;width:137px;height:35px;border-radius:3px;background:linear-gradient(#ff7a5a,#e3261a);color:#fff;font-size:20px;display:flex;align-items:center;justify-content:center;letter-spacing:-.5px}
.recent{position:absolute;left:626px;top:507px;width:312px;height:420px;background:#e4ecf5}
.recent-head{height:88px;background:linear-gradient(var(--orange-top),var(--orange-bottom));color:#111;font-size:23px;display:flex;align-items:center;justify-content:center}
.results{position:absolute;left:11px;top:99px;width:290px;font-size:12px;color:#222}
.results .cols{display:flex;font-weight:700;font-size:14px;margin-bottom:8px;letter-spacing:.5px}
.results .cols span,.results .row span{flex:1;text-align:center}
.results .row{display:flex;height:25px;align-items:center;margin-bottom:4.4px;border:1px solid #8b9bc4;border-radius:3px;background:linear-gradient(var(--row-top),var(--row-bottom));font-size:13.5px}
.social{position:absolute;left:706px;top:926px;display:flex;gap:19px}
.social-item{width:46px;text-align:center;font-size:8px;font-weight:700;color:#111}
.social-item i{display:block;width:46px;height:46px;border-radius:8px;background:linear-gradient(#4b7bd0,#1e4aa0);margin-bottom:4px}
.social-item.sky i{background:linear-gradient(#8fd6f2,#3aa6da)}
.site-footer{position:absolute;left:0;top:1027px;width:941px;text-align:center;font-size:12px;color:#1a2a55}
</style>
</head>
<body>
<header class="site-header">
  <div class="brand"><span class="brand-dot"></span><span class="brand-name">Ringbeacon Hub</span></div>
  <div class="tagline"><span class="site">Ringbeacon Hub</span><span class="role">VoIP CNAM Service Provider</span></div>
</header>
<div class="sheet">
  <nav class="main-nav">
    <a class="active" style="width:107px">Home</a>
    <a style="width:157px">About Us</a>
    <a style="width:172px">How to</a>
    <a style="width:190px">Pricing</a>
    <a style="width:164px">Support</a>
    <a style="width:151px;border-right:0">Contact us</a>
  </nav>

  <section class="content-panel">
    <h1>About Us</h1>
    <p>Ringbeacon Hub is a leading provider of CNAM / Caller ID Name services for VoIP providers and PBX systems. We support United States and Canadian phone numbers. Our service integrates seamlessly with all types of PBX systems including Pinwheel, tonebox, Voxality, Dialium, Flexistix, OpenSwitchPBX, LibreRoute and more!</p>
    <p>We have access to all of the major CNAM databases in the United States and Canada, something we're proud to offer.</p>
    <p>Use our easy to use examples to begin delivering caller ID name to your PBX or VoIP customers in minutes.</p>
    <p>Our super low rates, high quality results and unprecedented features set us apart from our competitors. You'll have no monthly fees, instant setup and automatic CNAM query price reductions based on your monthly query volume, features that our competitors simply don't provide!</p>
    <p>In addition to our already low prices, since we're so confident in the quality of our CNAM results in comparison to our competition, you'll pay a deeply discounted price per each query that returns an "UNAVAILABLE" result, saving you money!</p>
    <p><span class="accent">Sign up now</span> to begin your free trial account with 5 free CNAM lookups!</p>

    <div class="info-box" style="top:358px;height:220px">
      <div class="info-tab">What is CNAM?</div>
      <p>CNAM is a database of caller names used to identify the name of a caller when receiving an inbound call from the United States or Canada.</p>
      <p>The name of a caller is determined by searching a database for a name associated with the phone number of the calling party. You likely receive caller ID name produced by a lookup into a CNAM database on your land line phone service at home.</p>
      <p>Since the process of matching the caller's number to a CNAM database requires additional hardware and maitenence, it's likely that your VoIP provider does not provide caller ID name services with your inbound voice over IP calls, so you see only the number of the caller, preventing you from identifying the caller before you answer your calls.</p>
      <p>That's where Ringbeacon Hub comes in!</p>
    </div>

    <div class="info-box" style="top:627px;height:239px">
      <div class="info-tab">How can Ringbeacon Hub Help?</div>
      <p>Using our quick integration guides or free configuration assistance, you can start delivering caller ID name from our CNAM database sources in minutes so you can see who's calling. Our service is also a great way for VoIP service providers to give their customers caller ID name on inbound phone calls.</p>
      <p>Setup is quick and easy and your CNAM account features instant activation and a 5 free queries for testing your implementation.</p>
      <p>Since there are no monthly fees or account minimums, you have nothing to lose.</p>
      <p>To get started, click here to create your free account.</p>
      <p>If you need help setting up your PBX to work with our service, use the form in your administration panel after you signup.</p>
    </div>
  </section>

  <aside class="signup">
    <div class="signup-head"><span class="big">5 free</span><span class="small">CNAM lookups!</span></div>
    <div class="field" style="top:125px">Your Name....</div>
    <div class="field" style="top:174px">Your Number....</div>
    <div class="field" style="top:223px">Email Address....</div>
    <div class="field tall" style="top:273px">Your Comment....</div>
    <div class="signup-btn">Sign up Now</div>
  </aside>

  <aside class="recent">
    <div class="recent-head">Recent Query Results :</div>
    <div class="results">
      <div class="cols"><span>Phone Number</span><span>Caller ID name</span></div>
      <div class="row"><span>418885XXXX</span><span>XXXte GXXX</span></div>
      <div class="row"><span>418653XXXX</span><span>XXXEC XXX</span></div>
      <div class="row"><span>418688XXXX</span><span>XXX Phone XXX</span></div>
      <div class="row"><span>418872XXXX</span><span>XXXCIENNE-L XXX</span></div>
      <div class="row"><span>418658XXXX</span><span>XXXher GXXX</span></div>
      <div class="row"><span>418681XXXX</span><span>XXX Phone XXX</span></div>
      <div class="row"><span>418524XXXX</span><span>XXXEC XXX</span></div>
      <div class="row"><span>418873XXXX</span><span>XXXerc MauriXXX</span></div>
      <div class="row"><span>418387XXXX</span><span>XXXTERIA N JXXX</span></div>
      <div class="row"><span>418848XXXX</span><span>XXX Phone XXX</span></div>
    </div>
  </aside>

  <div class="social">
    <div class="social-item"><i></i>FRIENDWALL</div>
    <div class="social-item sky"><i></i>CHIRPLINE</div>
    <div class="social-item"><i></i>SPACEHUB</div>
  </div>

  <footer class="site-footer">[ Copyright 2011 Ringbeacon Hub | Brought to you by Northwire Labs ]</footer>
</div>
</body>
</html>
```